Brackenvale.com Postcard

We want to create a postcard, which is going to be mailed out to 6k managers at Hospitals throughout the USA.

I attached a rough draft of what I want the postcard to look like, but want it to look much better. The postcard size is 5.47" * 4.21"

```html
<!DOCTYPE html>
<html lang="en">
<head>
<meta charset="utf-8">
<title>Brackenvale Medical Postcard</title>
<link rel="stylesheet" href="https://fonts.googleapis.com/css2?family=Oswald:wght@600&family=Jost:wght@400;500;600&display=swap">
<style>
  :root {
    --backdrop: #177a3d;
    --card: #ffffff;
    --navy: #131f5c;
    --green: #0f6b35;
    --royal: #4a6cb2;
    --sky: #a9c4d6;
    --ink: #111111;
    --rule: #444444;
    --faint: #e9e9e9;
  }
  * { box-sizing: border-box; margin: 0; padding: 0; }
  html, body { width: 1037px; height: 1200px; overflow: hidden; }
  body {
    background: radial-gradient(ellipse at center, #0f5a2c 0%, var(--backdrop) 70%);
    font-family: "Jost", sans-serif;
    position: relative;
  }
  .card {
    position: absolute;
    background: var(--card);
    overflow: hidden;
  }
  .card--front { left: 169px; top: 37px; width: 695px; height: 533px; }
  .card--back { left: 165px; top: 594px; width: 702px; height: 543px; }
  .swoosh { position: absolute; inset: 0; width: 100%; height: 100%; }
  .brand {
    position: absolute;
    display: flex; align-items: center; gap: 10px;
    font-family: "Jost", sans-serif;
    font-weight: 500;
    color: var(--navy);
    text-transform: uppercase;
    letter-spacing: 1px;
    white-space: nowrap;
    font-size: 30px;
    line-height: 40px;
  }
  .brand__dot { width: 30px; height: 30px; border-radius: 50%; background: var(--navy); flex: none; }
  .card--front .brand { left: 152px; top: 42px; }
  .headline {
    position: absolute; left: 0; right: 0; text-align: center;
    font-family: "Oswald", sans-serif; font-weight: 600;
    color: var(--green);
  }
  .card--front .headline { top: 112px; font-size: 37px; }
  .front-phone {
    position: absolute; left: 0; right: 0; top: 186px; text-align: center;
    font-family: "Jost", sans-serif; font-weight: 600;
    font-size: 33px; color: var(--navy);
  }
  .pitch {
    position: absolute; left: 51px; top: 282px; width: 336px;
    font-size: 20px; line-height: 23.5px; color: var(--navy);
    text-align: justify; letter-spacing: 1px;
  }
  .product-photo {
    position: absolute; left: 404px; top: 232px; width: 194px; height: 220px;
    background: linear-gradient(160deg, #e9eef2 0%, #c9d3dc 55%, #d8a890 100%);
    border-radius: 10px;
  }
  .closing {
    position: absolute; left: 51px; top: 481px;
    font-size: 29px; color: var(--ink); white-space: nowrap;
  }
  .closing strong { color: var(--navy); font-weight: 600; }
  .card--back .brand { left: 86px; top: 80px; }
  .return-address {
    position: absolute; right: 192px; top: 24px; text-align: right;
    font-size: 15px; line-height: 20px; color: var(--ink);
  }
  .stamp-box {
    position: absolute; left: 529px; top: 38px; width: 126px; height: 136px;
    border: 1px solid #888;
  }
  .card--back .headline {
    top: 186px; left: 36px; right: auto; width: 290px;
    font-size: 35px; line-height: 49px; text-transform: uppercase;
  }
  .contact {
    position: absolute; left: 30px; width: 300px; top: 314px; text-align: center;
    color: var(--ink);
  }
  .contact__phone { font-weight: 600; font-size: 27px; line-height: 32px; }
  .contact__line { font-size: 20px; line-height: 27px; }
  .address-lines { position: absolute; left: 386px; width: 270px; top: 259px; }
  .address-lines span { display: block; border-top: 1px solid var(--rule); height: 49px; }
  .faint-mark {
    position: absolute; left: 80px; top: 482px;
    font-family: "Jost", sans-serif; font-weight: 500; font-size: 36px;
    text-transform: uppercase; letter-spacing: 1px; color: var(--faint);
    white-space: nowrap;
  }
</style>
</head>
<body>

<section class="card card--front">
  <svg class="swoosh" viewBox="0 0 695 533" aria-hidden="true">
    <path d="M0 0 H120 Q40 40 0 110 Z" fill="var(--royal)"/>
    <path d="M135 0 H175 Q40 90 0 300 V200 Q40 50 135 0 Z" fill="var(--sky)"/>
    <path d="M695 533 H590 Q660 490 695 420 Z" fill="var(--royal)"/>
    <path d="M560 533 H525 Q670 460 695 260 V350 Q670 480 560 533 Z" fill="var(--sky)"/>
  </svg>
  <div class="brand"><span class="brand__dot"></span>Brackenvale Medical</div>
  <h1 class="headline">Looking To Sell Your Infusion IV Pumps?</h1>
  <p class="front-phone">Call (555) 014 2870</p>
  <p class="pitch">Brackenvale Medical will purchase your infusion iv pumps. We will buy all of your quality iv pumps. We offer competitive pricing and will purchase from companies and individuals.</p>
  <div class="product-photo" role="img" aria-label="Photo of hands holding an infusion IV pump"></div>
  <p class="closing">Sell infusion pumps to <strong>Brackenvale Medical</strong> today!</p>
</section>

<section class="card card--back">
  <svg class="swoosh" viewBox="0 0 702 543" aria-hidden="true">
    <path d="M0 0 H110 Q40 35 0 100 Z" fill="var(--royal)"/>
    <path d="M125 0 H165 Q35 90 0 260 V180 Q35 45 125 0 Z" fill="var(--sky)"/>
    <path d="M338 168 Q340 420 175 449 H338 Z" fill="var(--sky)"/>
    <path d="M338 335 Q300 420 218 449 H338 Z" fill="var(--royal)"/>
  </svg>
  <p class="return-address">PO Box 2208<br>Fernridge, NC 27999</p>
  <div class="stamp-box"></div>
  <div class="brand"><span class="brand__dot"></span>Brackenvale Medical</div>
  <h2 class="headline">We Buy<br>Infusion IV Pumps</h2>
  <div class="contact">
    <p class="contact__phone">555 014 2870</p>
    <p class="contact__line">sales@brackenvale.com</p>
    <p class="contact__line">www.brackenvale.com</p>
  </div>
  <div class="address-lines"><span></span><span></span><span></span></div>
  <div class="faint-mark" aria-hidden="true">Brackenvale Medical</div>
</section>

</body>
</html>
```